Small consulting business needs logo and business card design

I need a logo, business card and letterhead design for a small consulting firm called Kestrawell Consulting. My customers are generally small to medium sized businesses but I have done work for major corporates and government departments. The field of consulting is strategic/business planning and program management. I have blue as the predominate colour in my current business card but I am happy to change this for the right design
Industry/Entity Type
Business

```html
<!DOCTYPE html>
<html lang="en">
<head>
<meta charset="utf-8">
<title>Kestrawell Consulting – Business Card</title>
<link href="https://fonts.googleapis.com/css2?family=Bree+Serif&family=Quantico:wght@400;700&display=swap" rel="stylesheet">
<style>
  :root {
    --bg-light: #f1f1f1;
    --bg-dark: #d6d6d6;
    --card-dark: #333234;
    --blue-light: #4fd0e0;
    --blue-mid: #29aee0;
    --blue-deep: #1a8fd0;
    --silver-light: #f4f4f4;
    --silver-dark: #a9a9ab;
    --ink-white: #ffffff;
    --ink-soft: #e9f7ff;
  }
  * { box-sizing: border-box; margin: 0; padding: 0; }
  html, body { width: 1200px; height: 475px; overflow: hidden; }
  body {
    background: radial-gradient(ellipse at center, var(--bg-light) 0%, var(--bg-dark) 100%);
    display: flex;
    align-items: center;
    justify-content: center;
    gap: 60px;
    font-family: "Quantico", sans-serif;
  }
  .card {
    position: relative;
    width: 520px;
    height: 297px;
    background: var(--card-dark);
    overflow: hidden;
    box-shadow: 0 6px 18px rgba(0,0,0,0.25);
  }
  .card-art { position: absolute; inset: 0; width: 100%; height: 100%; }
  .brand {
    position: absolute;
    color: var(--ink-white);
    font-family: "Bree Serif", serif;
    font-weight: 400;
    line-height: 1;
    letter-spacing: 1px;
  }
  .brand-name { display: block; font-size: 30px; text-transform: uppercase; }
  .brand-line { display: block; font-size: 34px; margin-top: 2px; }
  .front .brand { left: 34px; bottom: 40px; }
  .back .brand { left: 0; right: 0; top: 50%; transform: translateY(-50%); text-align: center; }
  .contact {
    position: absolute;
    right: 26px;
    top: 22px;
    width: 250px;
    text-align: right;
    color: var(--ink-white);
  }
  .person-name { font-size: 17px; letter-spacing: 1.5px; text-transform: uppercase; }
  .person-role { font-size: 11px; color: var(--ink-soft); margin-top: 2px; }
  .address { font-size: 11px; margin-top: 18px; line-height: 1.45; }
  .details { list-style: none; margin-top: 16px; font-size: 11px; }
  .details li {
    display: flex;
    justify-content: flex-end;
    align-items: center;
    gap: 8px;
    height: 19px;
  }
  .icon { width: 12px; height: 12px; fill: none; stroke: var(--ink-white); stroke-width: 1.4; }
</style>
</head>
<body>

  <section class="card front">
    <svg class="card-art" viewBox="0 0 520 297" preserveAspectRatio="none" aria-hidden="true">
      <defs>
        <radialGradient id="blueField" cx="0.72" cy="0.45" r="0.7">
          <stop offset="0" stop-color="var(--blue-light)"/>
          <stop offset="0.55" stop-color="var(--blue-mid)"/>
          <stop offset="1" stop-color="var(--blue-deep)"/>
        </radialGradient>
        <linearGradient id="silverBand" x1="0" y1="0" x2="1" y2="0">
          <stop offset="0" stop-color="var(--silver-dark)"/>
          <stop offset="0.5" stop-color="var(--silver-light)"/>
          <stop offset="1" stop-color="var(--silver-dark)"/>
        </linearGradient>
      </defs>
      <path class="silver-band" d="M200 0 C 300 70, 270 220, 216 297 L 520 297 L 520 0 Z" fill="url(#silverBand)"/>
      <path class="blue-field" d="M232 0 C 320 80, 300 220, 262 297 L 520 297 L 520 0 Z" fill="url(#blueField)"/>
    </svg>

    <div class="brand">
      <span class="brand-name">Kestrawell</span>
      <span class="brand-line">Consulting</span>
    </div>

    <div class="contact">
      <p class="person-name">Marcus Delane</p>
      <p class="person-role">Managing Director</p>
      <p class="address">Level 6, 14 Harbour Street NSX</p>
      <ul class="details">
        <li>021 555 0147
          <svg class="icon" viewBox="0 0 12 12"><path d="M3 1 L5 3.5 L4 5 Q5.5 7 7 8 L8.5 7 L11 9 L9.5 11 Q4 10 1 2.5 Z"/></svg>
        </li>
        <li>021 555 0148
          <svg class="icon" viewBox="0 0 12 12"><rect x="3" y="1" width="6" height="10" rx="1"/><line x1="5" y1="9.3" x2="7" y2="9.3"/></svg>
        </li>
        <li>hello@kestrawell.com
          <svg class="icon" viewBox="0 0 12 12"><rect x="1" y="2.5" width="10" height="7"/><path d="M1 2.5 L6 6.5 L11 2.5"/></svg>
        </li>
        <li>www.kestrawell.com
          <svg class="icon" viewBox="0 0 12 12"><circle cx="6" cy="6" r="5"/><ellipse cx="6" cy="6" rx="2.2" ry="5"/><line x1="1" y1="6" x2="11" y2="6"/></svg>
        </li>
      </ul>
    </div>
  </section>

  <section class="card back">
    <div class="brand">
      <span class="brand-name">Kestrawell</span>
      <span class="brand-line">Consulting</span>
    </div>
  </section>

</body>
</html>
```